CORVEN HIDEWORKS COLLECTIVE BUSINESS CARD
BUSINESS CARD
CORVEN HIDEWORKS COLLECTIVE BUSINESS CARD -
Creative Brief
Use specific fonts
Anything professional
Professional
Hal Durnsey
CEO
512 Wexbury Lane Manhasset, NY 11284, USA
hdurnsey@corvenhideworks.com
www.corvenhideworks.com
Please add "Alliance of Pelmora Hide Finishers" under our logo.

```html
<!DOCTYPE html>
<html lang="en">
<head>
<meta charset="utf-8">
<title>Corven Hideworks Collective Stationery</title>
<link href="https://fonts.googleapis.com/css2?family=Lato:wght@400;700&display=swap" rel="stylesheet">
<style>
:root{
  --backdrop:#d8b47e;
  --paper:#ffffff;
  --green-dark:#1d5427;
  --green-mid:#3d7d33;
  --green-light:#7fb24a;
  --ink:#333333;
  --ink-soft:#777777;
  --rule:#9a9a9a;
  --faint:#e4ecdf;
  --label:#3b2a14;
}
*{box-sizing:border-box;margin:0;padding:0}
html,body{width:1200px;height:562px;overflow:hidden;background:var(--backdrop);font-family:"Lato",sans-serif;color:var(--ink)}
.canvas{position:relative;width:1200px;height:562px}
.piece-label{position:absolute;font-size:7px;font-weight:700;color:var(--label);text-align:center}
.sheet{position:absolute;background:var(--paper);box-shadow:0 1px 3px rgba(0,0,0,.25);overflow:hidden}
.brand{display:flex;flex-direction:column;align-items:center;text-align:center}
.brand-mark{width:12px;height:12px;background:var(--green-dark);margin-bottom:4px}
.brand-name{font-weight:700;color:var(--green-dark);letter-spacing:.06em}
.brand-tagline{color:var(--ink-soft);margin-top:2px;letter-spacing:.04em}
.watermark{position:absolute;left:50%;transform:translateX(-50%);display:flex;flex-direction:column;align-items:center}
.watermark-square{width:120px;height:120px;background:var(--faint)}
.watermark-name{font-weight:700;color:var(--faint);font-size:13px;letter-spacing:.08em;margin-top:8px;white-space:nowrap}
.footer-line{position:absolute;left:0;right:0;text-align:center;font-size:5px;color:var(--ink-soft);letter-spacing:.03em}
/* fax */
.fax{left:19px;top:29px;width:377px;height:511px}
.fax .brand{margin-top:14px}
.fax-title{position:absolute;right:22px;top:92px;font-size:9px;font-weight:700;color:var(--ink)}
.fax-table{position:absolute;left:22px;top:106px;width:333px;border-collapse:collapse;font-size:7px}
.fax-table td{border:1px solid var(--rule);height:18px;padding:0 4px}
.fax-table .field{width:40px}
.fax-checks{position:absolute;left:22px;top:196px;display:flex;gap:22px;font-size:6px}
.fax-checks span{display:flex;align-items:center;gap:3px}
.fax-checks i{display:inline-block;width:6px;height:6px;border:1px solid var(--ink)}
/* letterhead */
.letterhead{left:408px;top:29px;width:372px;height:511px}
.letterhead-band{position:absolute;left:0;top:0;bottom:0;width:14px;background:linear-gradient(90deg,var(--green-dark),var(--green-light))}
.letterhead .brand{margin-top:18px;margin-left:14px}
/* cards */
.card{width:100px;height:60px;top:41px}
.card-one{left:792px;display:flex;align-items:center;justify-content:center}
.card-two{left:904px;padding:6px 7px}
.card-two .brand{align-items:flex-start;text-align:left}
.card-person{margin-top:7px;font-size:5px;line-height:1.4;color:var(--ink)}
.card-person strong{color:var(--green-dark)}
/* envelopes */
.envelope-front{left:792px;top:132px;width:392px;height:204px}
.envelope-front .brand{position:absolute;left:14px;top:12px;align-items:flex-start;text-align:left}
.return-address{position:absolute;left:14px;top:70px;font-size:5px;color:var(--ink-soft)}
.envelope-front .watermark{top:40px;left:auto;right:40px;transform:none}
.envelope-back{left:792px;top:365px;width:392px;height:175px}
.envelope-back svg{position:absolute;left:0;top:0}
</style>
</head>
<body>
<main class="canvas">

  <div class="piece-label" style="left:19px;top:15px;width:377px">Fax Cover</div>
  <section class="sheet fax">
    <div class="brand">
      <div class="brand-mark"></div>
      <div class="brand-name" style="font-size:8px">CORVEN HIDEWORKS COLLECTIVE</div>
      <div class="brand-tagline" style="font-size:4.5px">Alliance of Pelmora Hide Finishers</div>
    </div>
    <div class="fax-title">FAX</div>
    <table class="fax-table">
      <tr><td class="field">To:</td><td></td><td class="field">From:</td><td></td></tr>
      <tr><td class="field">Fax:</td><td></td><td class="field">Pages:</td><td></td></tr>
      <tr><td class="field">Phone:</td><td></td><td class="field">Date:</td><td></td></tr>
      <tr><td class="field">Re:</td><td></td><td class="field">CC:</td><td></td></tr>
    </table>
    <div class="fax-checks">
      <span><i></i>Urgent</span><span><i></i>For Review</span><span><i></i>Please Comment</span><span><i></i>Please Reply</span><span><i></i>Please Recycle</span>
    </div>
    <div class="watermark" style="top:255px">
      <div class="watermark-square"></div>
      <div class="watermark-name">CORVEN HIDEWORKS COLLECTIVE</div>
    </div>
    <div class="footer-line" style="bottom:26px">512 Wexbury Lane · Manhasset, NY 11284 · T 516.555.0142 · F 516.555.0143 · hdurnsey@corvenhideworks.com</div>
    <div class="footer-line" style="bottom:18px">www.corvenhideworks.com</div>
  </section>

  <div class="piece-label" style="left:408px;top:15px;width:372px">Letterhead</div>
  <section class="sheet letterhead">
    <div class="letterhead-band"></div>
    <div class="brand">
      <div class="brand-mark"></div>
      <div class="brand-name" style="font-size:8px">CORVEN HIDEWORKS COLLECTIVE</div>
      <div class="brand-tagline" style="font-size:4.5px">Alliance of Pelmora Hide Finishers</div>
    </div>
    <div class="watermark" style="top:240px;margin-left:7px">
      <div class="watermark-square"></div>
      <div class="watermark-name">CORVEN HIDEWORKS COLLECTIVE</div>
    </div>
    <div class="footer-line" style="bottom:26px;left:14px">512 Wexbury Lane · Manhasset, NY 11284 · T 516.555.0142 · F 516.555.0143</div>
    <div class="footer-line" style="bottom:18px;left:14px">www.corvenhideworks.com</div>
  </section>

  <div class="piece-label" style="left:792px;top:30px;width:100px">Business Card (Option 1)</div>
  <section class="sheet card card-one">
    <div class="brand">
      <div class="brand-mark" style="width:8px;height:8px;margin-bottom:3px"></div>
      <div class="brand-name" style="font-size:5px">CORVEN HIDEWORKS COLLECTIVE</div>
      <div class="brand-tagline" style="font-size:3.5px">Alliance of Pelmora Hide Finishers</div>
    </div>
  </section>

  <div class="piece-label" style="left:904px;top:30px;width:100px">Business Card (Option 2)</div>
  <section class="sheet card card-two">
    <div class="brand">
      <div class="brand-name" style="font-size:5px">CORVEN HIDEWORKS COLLECTIVE</div>
      <div class="brand-tagline" style="font-size:3.5px">Alliance of Pelmora Hide Finishers</div>
    </div>
    <div class="card-person"><strong>Hal Durnsey</strong><br>CEO<br>512 Wexbury Lane Manhasset, NY 11284, USA<br>hdurnsey@corvenhideworks.com</div>
  </section>

  <div class="piece-label" style="left:792px;top:120px;width:392px">Envelope (Front)</div>
  <section class="sheet envelope-front">
    <div class="brand">
      <div class="brand-mark" style="width:9px;height:9px"></div>
      <div class="brand-name" style="font-size:6px">CORVEN HIDEWORKS COLLECTIVE</div>
      <div class="brand-tagline" style="font-size:4px">Alliance of Pelmora Hide Finishers</div>
    </div>
    <div class="return-address">512 Wexbury Lane Manhasset, NY 11284</div>
    <div class="watermark">
      <div class="watermark-square" style="width:100px;height:100px"></div>
    </div>
  </section>

  <div class="piece-label" style="left:792px;top:353px;width:392px">Envelope (Back)</div>
  <section class="sheet envelope-back">
    <svg width="392" height="175" viewBox="0 0 392 175" aria-hidden="true">
      <defs>
        <linearGradient id="flapShade" x1="0" y1="0" x2="0" y2="1">
          <stop offset="0" stop-color="#1d5427"/>
          <stop offset="1" stop-color="#5f9a3c"/>
        </linearGradient>
      </defs>
      <path d="M0 0 H392 V22 L214 68 Q196 73 178 68 L0 22 Z" fill="url(#flapShade)"/>
    </svg>
  </section>

</main>
</body>
</html>
```